brightmesh Business Card

Already have the logo, but now need the business card design

Industry/Entity Type

Business Software

Contact Information for Business Card

web site will be brightmesh.io / The card should have the person name / position / mobile / email / and company address

Colors

Designer to choose colors to be used in the design.

Requirements
Must have
• See business card details
• One side to have the brightmesh logo
Nice to have
• If possible the 'O' from flow can be watermarked into the second side
• Try to fit in the words brightmesh Business Solutions

```html
<!DOCTYPE html>
<html lang="en">
<head>
<meta charset="utf-8">
<title>brightmesh Business Card</title>
<link rel="stylesheet" href="https://fonts.googleapis.com/css2?family=Work+Sans:wght@400;500;600&display=swap">
<style>
  :root {
    --bg: #2a2a2c;
    --red: #e0202a;
    --red-deep: #b3141c;
    --grey-text: #555558;
    --grey-logo: #6e6e72;
    --grey-line: #7a7a7e;
    --grey-light: #c9c9cc;
    --white: #ffffff;
    --paper-shade: #ececee;
  }
  * { margin: 0; padding: 0; box-sizing: border-box; }
  html, body { width: 1200px; height: 900px; overflow: hidden; }
  body {
    background: var(--bg);
    font-family: "Work Sans", Arial, sans-serif;
    position: relative;
  }
  .card {
    position: absolute;
    left: 270px;
    width: 660px;
    height: 377px;
    overflow: hidden;
    box-shadow: 0 14px 30px rgba(0,0,0,.45);
  }
  .card-front {
    top: 50px;
    background: linear-gradient(135deg, var(--paper-shade) 0%, var(--white) 45%, var(--white) 100%);
  }
  .card-back {
    top: 473px;
    background: linear-gradient(135deg, var(--red-deep) 0%, var(--red) 55%, var(--red-deep) 100%);
  }
  .wave { position: absolute; inset: 0; width: 100%; height: 100%; }
  .person { position: absolute; left: 42px; top: 52px; }
  .person-name {
    color: var(--red);
    font-size: 24px;
    font-weight: 500;
    letter-spacing: .5px;
    text-transform: uppercase;
    line-height: 1.1;
  }
  .person-role { color: var(--grey-text); font-size: 15px; margin-top: 2px; letter-spacing: .5px; }
  .divider {
    position: absolute;
    left: 42px; top: 120px;
    width: 560px; height: 1.5px;
    background: var(--red);
  }
  .contact { position: absolute; left: 42px; top: 134px; list-style: none; }
  .contact li {
    display: flex; align-items: center; gap: 9px;
    color: var(--grey-text);
    font-size: 15px;
    letter-spacing: .8px;
    line-height: 24px;
  }
  .contact svg { width: 11px; height: 11px; flex: none; }
  .contact .accent { color: var(--red); font-weight: 500; }
  .brand { position: absolute; right: 46px; top: 26px; }
  .brand-name {
    color: var(--grey-logo);
    font-size: 58px;
    font-weight: 400;
    letter-spacing: -1.5px;
    line-height: 1;
  }
  .brand-tagline {
    color: var(--grey-text);
    font-size: 16px;
    letter-spacing: 5px;
    margin-top: 4px;
  }
  .address {
    position: absolute; right: 46px; top: 146px;
    text-align: right;
    font-style: normal;
    color: var(--grey-text);
    font-size: 16px;
    letter-spacing: 1px;
    line-height: 24px;
  }
  .back-brand {
    position: absolute; inset: 0;
    display: flex; align-items: center; justify-content: center;
    color: var(--grey-light);
    font-size: 96px;
    font-weight: 400;
    letter-spacing: -2px;
  }
</style>
</head>
<body>
  <section class="card card-front">
    <svg class="wave" viewBox="0 0 660 377" preserveAspectRatio="none" aria-hidden="true">
      <path d="M0 240 C 150 292, 300 282, 370 320 C 410 342, 425 360, 430 377 L 0 377 Z" fill="var(--red)"/>
      <path d="M0 231 C 150 283, 306 273, 379 313 C 421 337, 437 358, 442 377" fill="none" stroke="var(--grey-line)" stroke-width="4"/>
    </svg>

    <div class="person">
      <h1 class="person-name">Daniel Reeve</h1>
      <p class="person-role">Director</p>
    </div>
    <div class="divider"></div>

    <ul class="contact">
      <li>
        <svg viewBox="0 0 12 12"><path d="M3 1 L5 3.5 L4 5 Q5.5 7.5 7 8 L8.5 7 L11 9 L9.5 11 Q3 10 1 2.5 Z" fill="var(--red)"/></svg>
        (514) 555-0142
      </li>
      <li>
        <svg viewBox="0 0 12 12"><rect x="1" y="2.5" width="10" height="7" fill="none" stroke="var(--red)" stroke-width="1.3"/><path d="M1 2.5 L6 6.5 L11 2.5" fill="none" stroke="var(--red)" stroke-width="1.3"/></svg>
        info@brightmesh.io
      </li>
      <li>
        <svg viewBox="0 0 12 12"><circle cx="6" cy="6" r="5" fill="none" stroke="var(--red)" stroke-width="1.3"/><path d="M1 6 H11 M6 1 Q3 6 6 11 M6 1 Q9 6 6 11" fill="none" stroke="var(--red)" stroke-width="1"/></svg>
        <span>www.<span class="accent">brightmesh</span>.io</span>
      </li>
    </ul>

    <div class="brand">
      <div class="brand-name">brightmesh</div>
      <div class="brand-tagline">Business Solutions</div>
    </div>

    <address class="address">
      248b Harlow Street,<br>
      Christchurch, NZ, 8011
    </address>
  </section>

  <section class="card card-back">
    <div class="back-brand">brightmesh</div>
  </section>
</body>
</html>
```